Need posters that inspire entrepreneurs

I want to create beautiful, inspiring wall art. I'm looking for a designer to create an awesome sample (note this sample is not for real use). The winning design will form the foundation of our art "style" so there will be LOTS of ongoing work for the winning designer.

It's your challenge to create a style that is clean, inspiring and timeless, and possibly can be adapted to different colour palettes.

Looking for a perfect execution of words, image and design.

The attached example shows one idea. It should serve as an idea only.

Format of the images should be either rectangular or square. Exact size is preferably UK A4 (US letter) or max A3. Assume that a display would consist of a 4 x 4 image grid so size needs to allow for that in a small to medium size office.

The quotes I want in the 3 samples (each in an individual poster - not combined in 1 poster). Each quote should have it's own, the reason for three is to prove the design work on more than one quote. The quotes are:

1) Failure is the condiment that gives success its flavor.
– Wendell Ruskin

2) Whether you think you can or think you can’t, you’re right.
– Milo Dagwell

3) Ever tried. Ever failed. No matter. Try Again. Fail again. Fail better.
– Oswin Tarrant

Each design should include the image of the person and the quote + any design elements you consider relevant. You should find relevant images of the individuals being quoted. The final images will not be published or used commercially in any way.

Font styles to use
Serif
Sans Serif

Colors

Designer to choose colors to be used in the design.

Requirements
Must have
• Words and headshot image - 1 per poster design.
• Please consider in the design that there will not always be photographs of the person quoted and as such the design will need to hold, whether the source is a photo, sketch or something else.
Nice to have
• None, but note that the final image will be printed on a wall mounted board, printed to the edge but not on the edge. The board will have black or white edges so consider in the design.
Should not have
• None

```html
<!DOCTYPE html>
<html lang="en">
<head>
<meta charset="UTF-8">
<title>Quote Poster – Milo Dagwell</title>
<link href="https://fonts.googleapis.com/css2?family=Roboto+Condensed:wght@700&display=swap" rel="stylesheet">
<style>
  :root {
    --poster-bg: #000000;
    --quote-ink: #d4d4d4;
    --byline-ink: #9a9a9a;
    --portrait-light: #6a6a6a;
    --portrait-mid: #3a3a3a;
    --portrait-dark: #1c1c1c;
  }
  html, body {
    margin: 0;
    padding: 0;
    width: 925px;
    height: 1200px;
    overflow: hidden;
    background: var(--poster-bg);
  }
  .poster {
    position: relative;
    width: 925px;
    height: 1200px;
    background: var(--poster-bg);
    overflow: hidden;
    font-family: "Roboto Condensed", "Arial Narrow", sans-serif;
  }
  .portrait {
    position: absolute;
    left: 290px;
    top: 440px;
    width: 635px;
    height: 760px;
    border-radius: 46% 46% 0 0 / 22% 22% 0 0;
    background:
      radial-gradient(ellipse 34% 22% at 46% 24%, var(--portrait-light) 0%, var(--portrait-mid) 70%, transparent 100%),
      linear-gradient(180deg, var(--portrait-mid) 0%, var(--portrait-dark) 55%, #121212 100%);
  }
  .quote {
    position: absolute;
    top: 46px;
    left: 0;
    width: 925px;
    margin: 0;
    text-align: center;
    color: var(--quote-ink);
    font-weight: 700;
    font-size: 72px;
    line-height: 80px;
    letter-spacing: 1.5px;
    text-transform: uppercase;
  }
  .quote span { display: block; }
  .byline {
    position: absolute;
    left: 95px;
    top: 1112px;
    margin: 0;
    color: var(--byline-ink);
    font-weight: 700;
    font-size: 40px;
    line-height: 48px;
    letter-spacing: 0.5px;
  }
</style>
</head>
<body>
  <main class="poster">
    <div class="portrait" role="img" aria-label="Black and white portrait of Milo Dagwell in a dark suit and white collar"></div>
    <blockquote class="quote">
      <span>Whether you think</span>
      <span>you can</span>
      <span>or</span>
      <span>think you can’t,</span>
      <span>you’re right</span>
    </blockquote>
    <p class="byline">Milo Dagwell</p>
  </main>
</body>
</html>
```